Plastering (solid plastering) business card design

We need a business card for a a small plastering business based in Perth Western Australia. We are a small team that provides a service in solid plastering specialising in float, white set and sand finish. We would like to see a clean business card with our name "Brightline Plastering" being the focus of the card and maybe incorporated into a logo. We don't have a logo at the moment so we would like to see some cards that may provide us with our future logo.

Industry/Entity Type

Business

Contact Information for Business Card

Brightline Plastering

Solid Plastering Specialists

Ph: Corey 0417683091
Ph: Liam 0468120357

Requirements
Should not have
• The design should not have Drywall incorporated into the card. In perth W.A. Plastering in different to someone that puts up Plyvane. We use sand, cement, lime and hardwall plaster.

```html
<!DOCTYPE html>
<html lang="en">
<head>
<meta charset="utf-8">
<title>Brightline Plastering – Business Card</title>
<link rel="stylesheet" href="https://fonts.googleapis.com/css2?family=Montserrat:wght@400;800&display=swap">
<style>
  :root {
    --backdrop: #c8c8c8;
    --card: #f4f4f3;
    --ink: #6d6d6d;
    --ink-soft: #5a5a5a;
    --gold: #c9b279;
  }
  html, body {
    margin: 0;
    width: 1200px;
    height: 873px;
    overflow: hidden;
    background: var(--backdrop);
  }
  .canvas {
    position: relative;
    width: 1200px;
    height: 873px;
    display: flex;
    align-items: center;
    justify-content: center;
  }
  .business-card {
    width: 700px;
    height: 400px;
    background: var(--card);
    box-shadow: 0 10px 30px rgba(0, 0, 0, 0.18);
    display: flex;
    flex-direction: column;
    align-items: center;
    justify-content: center;
    box-sizing: border-box;
    padding: 36px 70px;
    font-family: "Montserrat", sans-serif;
    color: var(--ink);
  }
  .brand-mark {
    width: 70px;
    height: 70px;
    background: var(--gold);
    margin-bottom: 20px;
  }
  .brand-name {
    margin: 0;
    font-weight: 800;
    font-size: 38px;
    letter-spacing: 1px;
    text-transform: uppercase;
    color: var(--ink);
    white-space: nowrap;
  }
  .tagline {
    margin: 6px 0 30px;
    font-weight: 400;
    font-size: 21px;
    letter-spacing: 3px;
    color: var(--ink-soft);
  }
  .contacts {
    width: 100%;
    display: flex;
    justify-content: space-between;
    padding: 0 20px;
    box-sizing: border-box;
  }
  .contact {
    display: flex;
    flex-direction: column;
    align-items: center;
    font-size: 18px;
    letter-spacing: 4px;
    color: var(--ink-soft);
    line-height: 1.6;
  }
</style>
</head>
<body>
  <main class="canvas">
    <section class="business-card">
      <div class="brand-mark" aria-hidden="true"></div>
      <h1 class="brand-name">Brightline Plastering</h1>
      <p class="tagline">Solid Plastering Specialists</p>
      <div class="contacts">
        <div class="contact">
          <span class="contact-name">Corey</span>
          <span class="contact-phone">0417683091</span>
        </div>
        <div class="contact">
          <span class="contact-name">Liam</span>
          <span class="contact-phone">0468120357</span>
        </div>
      </div>
    </section>
  </main>
</body>
</html>
```